Financing service for small businesses

Need a flyer design promoting our Financing Service, look at the attachment to see the services we offer.
We are a CPA firm and provide a wide range of services including advisory services to small businesses that are trying to obtain bank financing.
The flyer should grab the attention of prospective businesses who need assistant with their financing needs.

Target Market(s)

Small Businesses

Industry/Entity Type

It Service

Font styles to use
Serif

Colors

Designer to choose colors to be used in the design.

Requirements
Must have
• Our Logo and address
• Why use our services
• Look Professional

```html
<!DOCTYPE html>
<html lang="en">
<head>
<meta charset="utf-8">
<title>Business Financing Services Flyer</title>
<link href="https://fonts.googleapis.com/css2?family=Oswald:wght@600&family=Source+Sans+3:wght@400;600;700&display=swap" rel="stylesheet">
<style>
  :root{
    --blue:#2b63ad;
    --blue-dark:#1f4f93;
    --ink:#2b2b2b;
    --paper:#ffffff;
    --backdrop:#e9eaec;
    --photo-a:#4d5d78;
    --photo-b:#b9c3d3;
  }
  *{margin:0;padding:0;box-sizing:border-box}
  html,body{width:1200px;height:960px;overflow:hidden;background:var(--backdrop)}
  body{position:relative;font-family:"Source Sans 3",Arial,sans-serif;color:var(--ink)}
  .page{position:absolute;top:80px;width:570px;height:800px;background:var(--paper);box-shadow:0 4px 18px rgba(0,0,0,.18);overflow:hidden}
  .page--front{left:20px}
  .page--back{left:610px;padding:22px 24px 0 24px}
  .hero{position:absolute;left:0;top:0;width:570px;height:520px}
  .front-copy{position:absolute;left:34px;top:526px;right:30px;font-size:9.4px;line-height:1.32}
  .title{font-family:"Oswald",Impact,sans-serif;font-weight:600;color:var(--blue);font-size:21px;line-height:1.1;margin-bottom:10px}
  .front-copy p{margin-bottom:7px}
  .front-copy ul{list-style:none;margin-bottom:7px}
  .front-copy li::before,.back-list li::before{content:"• "}
  .front-copy li{padding-left:6px;text-indent:-6px}
  .lead{color:var(--blue)}
  .contact-bar{position:absolute;left:0;right:0;bottom:0;height:40px;background:var(--blue);color:#fff;display:flex;align-items:center;gap:14px;padding-left:40px;font-size:11px}
  .contact-bar .item{display:flex;align-items:center;gap:6px}
  .contact-bar .sep{opacity:.8}
  .contact-bar svg{width:11px;height:11px;fill:#fff}
  .top-rule{position:absolute;left:0;top:30px;width:430px;height:3px;background:var(--blue)}
  .brand{position:absolute;right:24px;top:16px;display:flex;align-items:center;gap:8px;font-size:13px;font-weight:600;color:var(--blue);letter-spacing:.06em}
  .brand .mark{width:26px;height:26px;background:var(--blue)}
  .back-body{margin-top:30px;font-size:8.6px;line-height:1.3}
  .back-body h2{font-family:"Oswald",Impact,sans-serif;font-weight:600;color:var(--blue);font-size:19px;line-height:1.15;margin:8px 0 3px}
  .back-body h2:first-child{margin-top:0}
  .back-body h3{font-size:8.8px;font-weight:700;margin-bottom:3px}
  .back-body p{margin-bottom:5px}
  .back-list{list-style:none;margin-bottom:4px}
  .back-list li{margin-bottom:2px}
  .small{font-size:7px}
</style>
</head>
<body>

<section class="page page--front">
  <svg class="hero" viewBox="0 0 570 520" aria-hidden="false">
    <defs>
      <linearGradient id="photoTone" x1="0" y1="0" x2="1" y2="1">
        <stop offset="0" stop-color="var(--photo-b)"/>
        <stop offset=".55" stop-color="var(--photo-a)"/>
        <stop offset="1" stop-color="#3a475d"/>
      </linearGradient>
    </defs>
    <path d="M0,0 L120,0 C80,120 72,300 125,410 C170,490 250,515 300,518 C200,525 95,470 45,360 C12,280 0,170 0,120 Z" fill="var(--blue)"/>
    <path d="M130,0 L570,0 L570,515 L260,515 C165,490 105,400 100,270 C96,150 112,60 130,0 Z" fill="url(#photoTone)" role="img" aria-label="Photo of a businessman in a grey suit holding up a business card"/>
    <path d="M60,330 C90,440 170,505 300,515" stroke="var(--blue)" stroke-width="2" fill="none"/>
  </svg>

  <div class="front-copy">
    <h1 class="title">Business Financing Services Calgary &amp; Vancouver</h1>
    <p>Financing is a key consideration for every business and is an integral part of allowing the business to properly plan for its future and realize its potential.</p>
    <p>Businesses require financing for many purposes, including;</p>
    <ul>
      <li>Asset Purchases (expand the capacity of your existing business by investing in equipment)</li>
      <li>Working Capital (helping to manage the short term cash flow pain that comes with increased business, usually from having to carry more inventory or a larger receivable balance from customers)</li>
      <li>Growth Capital (investing in expanding the your company's product or service offering)</li>
      <li>Mergers &amp; Acquisitions (acquiring another company to increase the size or scale of your business)</li>
      <li>Corporate Restructuring and Refinancing</li>
    </ul>
    <p class="lead">When considering financing alternatives it is important to have an advisor that fully understands your company and its needs as well as the market in order to ensure the following:</p>
    <ul>
      <li>Maximize the probability of obtaining the optimal financing</li>
      <li>The right amount of financing</li>
      <li>The most favorable terms</li>
      <li>The most reasonable cost of financing (there are often fees associated with the transaction which must be considered in addition to the interest rate on a debt instrument)</li>
      <li>The best source of financing (lender or investor)</li>
    </ul>
  </div>

  <footer class="contact-bar">
    <span class="item"><svg viewBox="0 0 10 10"><path d="M5 0a3.5 3.5 0 0 0-3.5 3.5C1.5 6 5 10 5 10s3.5-4 3.5-6.5A3.5 3.5 0 0 0 5 0zm0 5a1.5 1.5 0 1 1 0-3 1.5 1.5 0 0 1 0 3z"/></svg>410-2280 Ridgeline Avenue SE, Calgary, AB, T2H 3M7</span>
    <span class="sep">|</span>
    <span class="item"><svg viewBox="0 0 10 10"><path d="M2 0h2l1 2.5-1.3 1a6 6 0 0 0 2.8 2.8l1-1.3L10 6v2a2 2 0 0 1-2 2C3.6 10 0 6.4 0 2a2 2 0 0 1 2-2z"/></svg>(403) 555-0184</span>
    <span class="sep">|</span>
    <span class="item"><svg viewBox="0 0 10 10"><path d="M2 0h6v3H2zM0 4h10v5H0zm2 2v2h6V6z"/></svg>(403) 555-0197</span>
  </footer>
</section>

<section class="page page--back">
  <div class="top-rule"></div>
  <div class="brand"><span class="mark"></span>NORTHVALE</div>

  <div class="back-body">
    <h2>Financing Types</h2>
    <p>The types of financing used to meet financing needs might include:</p>
    <ul class="back-list">
      <li>Conventional Term Loans (a loan that is paid back over a specific period of time, usually offered by one of the Big Banks)</li>
      <li>Operating Loans (normally used for working capital, the balance usually fluctuates with the business</li>
      <li>Revolving Lines of Credit</li>
      <li>Project Financing <span class="small">(secured and used to fund a very specific activity of the business)</span></li>
      <li>Factoring <span class="small">(often used against accounts receivable in order to turn receivables to cash more quickly than simply waiting for the customer to pay)</span></li>
      <li>Subordinated Debt</li>
      <li>Venture Capital</li>
      <li>Angel Capital</li>
    </ul>

    <h2>What is the financing process</h2>
    <h3>Review and Assessment of the Business</h3>
    <p>Investors and lenders usually have a multitude of different financing proposals and opportunities that they are considering at any point in time. Due to the volume of potential opportunities, they must assess financing opportunities quickly to identify if they warrant further review. They often review key elements of a proposal and measure these elements against their own internal criteria. If your business or financing opportunity does not appear suitable for them, it is often difficult to get their attention again. We know what investors and lenders are looking for and we can make sure that your proposal is ideally suited for the particular lender or investor. It is important to address the strengths and weaknesses of your financing opportunity adequately in order to understand and address the investors' or lenders' key concerns. To obtain financing you must be investment ready. The review and assessment of your business is designed to go through your business and financing opportunity and your presentation to determine your investment readiness. Northvale would then provide recommendations as to how to improve your readiness and enhance your prospects of financing success. This step in the financing process involves obtaining and reviewing your financing package and supporting information, and interviewing you and possibly other key individuals. We assess your business and financing opportunity and the way they are presented, both from the perspective of how well they meet investor/lender criteria and how compelling the proposal and presentation are. We identify strengths and weaknesses, and make specific recommendations to you as to how they might be addressed and your investment readiness improved. Armed with this assessment, you can proceed to structure and develop a financing proposal with increased confidence of financing success.</p>

    <h2>Developing a Financing Proposal</h2>
    <h3>Review and Assessment of the Business</h3>
    <p>There are often many different financing options and these options can be structured in a variety of ways depending on the requirements of the business. Without the appropriate structure, you may not qualify for the financing you are interested in, your terms may not be as favorable or it may take more time than necessary. In order to optimize the process, we will work with you to determine the right type or combination of financing and financing structures.</p>
    <p>Investors and lenders review financing proposals very quickly and are looking for certain key elements. In most cases you have only one chance to get and keep their attention. If your proposal does not adequately tell your story, and does not appear to warrant further time, you may lose any chance you had to succeed with them. You need a proposal that is professional, compelling and complete.</p>
    <p>Developing a financing proposal involves considering and modeling alternate financing types and structures, and in some cases alternate corporate structures. Northvale will work with you to weigh the pros and cons of each alternative. This analysis will then be used to identify the most suitable financing type and structure for your business. Northvale will then prepare a Confidential Information Summary (CIS) in a format tailored for your financing opportunities. The CIS goes through the proposed transaction, addresses all relevant factors and provides the required supporting documentation. The CIS highlights the strengths of the proposal, explains how any weaknesses are mitigated, and conveys how your organization meets the prospective lender's or investor's criteria. Armed with the CIM, the financing placement process can begin.</p>

    <h2>Financing Placement</h2>
    <p>Investors and lenders will often accept proposals from almost anyone, however this does not mean that all proposals have an equal opportunity of being funded. Potential investors and lenders will often give more credibility to a proposal that comes from a source that they are familiar with and whom they trust. Northvale regularly works with both financial institutions and individual investors and therefore has access to the networks and contacts that increase the likelihood of success of your proposal. As a business owner seeking financing, you also need to consider that the best possible investor or lender for your business may not be accessible to you at all. This is where Northvale's network of financial institutions and investors can be leveraged to provide the best possible outcome. For optimal financing, you need to obtain the right financing from the right investor or lender with the right terms, in an appropriate time frame. With Northvale's Financing Placement we help you succeed with your financing objectives.</p>
    <p>Financing Placement involves: identifying and surveying prospective lenders and investors to determine the best sources of financing; presenting the proposal; and, monitoring and facilitating the information exchange process, negotiating between and communicating with the parties, and working towards a financing commitment with the best possible terms.</p>
  </div>
</section>

</body>
</html>
```